Squarespace website build: Quirk literary annual (initial design work supplied)

Our brand guidelines provide the look and feel for the website - we just need someone to create it based on our mock ups!
PLEASE NOTE:
- Please base our website off the website pages within the brief (ie homepage is GREEN)
- please ensure each page will be standalone (not a scrolling home page)
- please only use filtered duotone style photography as a hold, if you think the page needs a photo.
-please not the websites i have provided as an influence - especially TIDE YEARLY. We want very little photography.

Quirk is a literary and arts journal that provides a platform for both emerging and established writers and artists from New Zealand and beyond. We are passionate about sharing insights into the intimate and unique worlds of creatives with short stories, poetry, and art – showcasing raw and unfiltered glimpses into their world.

We have our brand guidelines and logo finalised, with a 'look and feel' design for the website within our attached brand guidelines document. We just need someone to design this simple website on Squarespace for us. It will have five pages and will need a newsletter sign up link:
Home page
About us page
Submissions page
Purchase page
Contact page

DRAFT WEB COPY

ABOUT
QUIRK is an independent literary annual journal established in 2022 by Hazel Wintergate and Mereana Clift that publishes unrepentant unfiltered accounts of life, eclectic takes on the mundane ordinary, and deep dives into modern love & sexuality.
Founder, Editor: Hazel Arohanui Wintergate
Founder, Production Director: Mereana Clift
Art Direction: Lorna Pike
Editorial Assistant: Kirsten Holloway-Dunn

I suggest duotone fashion-esque photography which is very Vesna Kordell/ Palm Springs vibe but not obviously identifiable.
· I love the style of Rufus Tennick for our shoot in particular. Group lazing around a pool, leisurely, glam, but effortless and ironically looking very natural – as though – yes, these are our lives.
SUBMISSION PAGE
Quirk welcomes submissions all year round.
We are drawn to dark humour, satirical takes on the social scene, and starkly honest accounts of ordinary life. Diversity is celebrated, adversity is welcomed and, above all, personal expression is championed. We are particularly seeking content that takes risks, screams of honesty and celebrates life’s most extraordinary moments.
Selected works will be published in our annual publication.

Submission guidelines
We accept flash fiction, short stories and poetry. Individual entries not to mustn’t exceed 2000 words.
Submitted work must be unpublished and in English. We welcome simultaneous submissions, but must be notified immediately if your manuscript is accepted for publication elsewhere or appears in any print or online source. We will endeavour to respond to all submissions within four weeks.
Please send submissions as a word document along with a brief bio of 50 words to pages@quirkjournal.test
PO Box[EB2]
​Note on Copyright: Copyright remains with the author.

Annual short story competition
Volume Alpha is interested in all that is spiritual, coincidental, or mysterious. Stories selected for this issue reflect life’s uncanny moments, those that defy explanation, and experiences that promote personal and spiritual growth. Entires must be no longer than 2000 words.

First prize: 1000
Second prize: 500
Third prize: 200[EB3]

SUPPORT US
Since our launch in 2022, we have relied upon the generous support of our creative business community in Wellington City, New Zealand. If you read us, or love our ethos, please consider a donation.
Link to chipinhere page
Updates

Hello designers
I would ideally love to have someone turn this around within a few weeks, because the design work has mostly been provided.
Thanks
Hazel

Hi everyone Please ensure you read our brand guidelines and follow the brief. Please note we do not yet have a product, as this is a new venture, so there is no point including images of a magazine that doesn't yet exist. Some further comment to ensure we get there: - We want all pages to be separate pages (not a scrolling home page) with a different colour based on the guidelines - The home page must look just as it does in the brand guidelines - There is no archive page (please read brief) as we have no archive yet. The pages are: Home, About, Contact, Competitions and submissions Thank you

Target Market(s)

writers and creatives

Industry/Entity Type

Writing/ creative/ publishing

Coding

Coded - Design and coding required

Number of Pages Required

4 page

Font styles to use
Other font styles liked:
• COTTA and Univers - as per brand guidelines

Requirements
Must have
• Squarespace designer needed to design our mocked up webpages.
Nice to have
• As close to the brand guideline mock ups as possible (see page 11,12,13)
Should not have
• anything outside of the brand guidelines

```html
<!DOCTYPE html>
<html lang="en">
<head>
<meta charset="utf-8">
<title>Quirk — Home</title>
<link rel="stylesheet" href="https://fonts.googleapis.com/css2?family=Playfair+Display:wght@400;700&family=Oswald:wght@500&family=Figtree:wght@400&display=swap">
<style>
:root{
  --green:#5f7a33;
  --gold:#b9a024;
  --gold-btn:#b49c22;
  --nav-gold:#d2b33e;
  --purple:#6b3f63;
  --pink:#bb5672;
  --cream:#f4f0e4;
  --white:#ffffff;
  --serif:"Playfair Display", Georgia, serif;
  --cond:"Oswald", "Arial Narrow", sans-serif;
  --sans:"Figtree", Helvetica, Arial, sans-serif;
}
*{margin:0;padding:0;box-sizing:border-box}
html,body{width:1200px;height:3766px;overflow:hidden}
body{position:relative;font-family:var(--sans);color:var(--white)}
.band{position:absolute;left:0;width:1200px}
.abs{position:absolute}
.wordmark{font-family:var(--serif);font-weight:400;color:var(--gold);font-size:56px;line-height:1;letter-spacing:1px}
.nav a{position:absolute;top:38px;font-family:var(--cond);font-weight:500;font-size:17px;color:var(--white);text-decoration:none;letter-spacing:.3px}
.nav a.current{color:var(--nav-gold)}
.hero-frame{left:131px;top:124px;width:939px;height:500px;border:2px solid var(--gold)}
.hero-art{left:137px;top:133px;width:927px;height:482px;background:linear-gradient(135deg,#1c4a6b 0%,#4a9aa8 35%,#16385a 60%,#6fb8b4 85%,#1d4665 100%)}
.hero-title{left:137px;top:285px;width:900px;text-align:center;font-family:var(--serif);font-weight:700;font-size:41px;line-height:46px;letter-spacing:-.5px}
h2.section-title{font-family:var(--serif);font-weight:700;font-size:32px;line-height:44px}
.catalogue-title{left:0;top:706px;width:1200px;text-align:center}
.cover{position:absolute;width:277px;height:369px;box-shadow:4px 6px 10px rgba(0,0,0,.25)}
.cover .issue,.cover .date{position:absolute;top:60px;font-family:var(--cond);font-size:11px}
.cover .issue{left:26px}.cover .date{right:26px}
.cover .name{position:absolute;top:34px;left:0;width:100%;text-align:center;font-family:var(--serif);font-size:54px;line-height:1}
.cover .art{position:absolute;left:20px;top:126px;width:237px;height:243px}
.cover-cream{background:var(--cream)}.cover-pink{background:var(--pink)}.cover-green{background:var(--green)}
.book-label{position:absolute;width:277px;text-align:center;font-family:var(--serif);font-weight:700;font-size:24px}
.photo{position:absolute}
.body-copy{font-size:16px;line-height:24px}
.btn{position:absolute;display:flex;align-items:center;justify-content:center;font-family:var(--cond);font-weight:500;font-size:17px;color:var(--white);text-decoration:none;height:44px;width:117px}
.btn-gold{background:var(--gold-btn)}
.btn-purple{background:var(--purple)}
.card-title{position:absolute;width:443px;text-align:center;font-family:var(--serif);font-weight:700;font-size:27px}
.card-copy{position:absolute;width:360px;text-align:center;font-size:16px;line-height:21px}
.foot-links a{position:absolute;font-family:var(--cond);font-weight:500;font-size:17px;color:var(--white);text-decoration:none}
</style>
</head>
<body>

<header class="band" style="top:0;height:671px;background:var(--green)">
  <div class="abs wordmark" style="left:131px;top:16px">quirk</div>
  <nav class="nav">
    <a class="current" href="#" style="left:557px">HOME</a>
    <a href="#" style="left:636px">ABOUT US</a>
    <a href="#" style="left:747px">SUBMISSIONS</a>
    <a href="#" style="left:890px">PURCHASE</a>
    <a href="#" style="left:1007px">CONTACT</a>
  </nav>
  <div class="abs hero-frame"></div>
  <div class="abs hero-art" role="img" aria-label="Marbled blue and teal fluid-paint artwork"></div>
  <h1 class="abs hero-title">Quirk is a plucky little<br>pubication out of Wellington,<br>New Zealand–give it a read here</h1>
</header>

<section class="band" style="top:671px;height:1089px;background:var(--gold)">
  <h2 class="abs section-title" style="left:0;top:35px;width:1200px;text-align:center">Our back catalogue is available<br>in digital format for a reduced price.</h2>

  <div class="cover cover-cream" style="left:156px;top:172px">
    <span class="issue" style="color:var(--pink)">ISSUE 001</span><span class="name" style="color:var(--green)">quirk</span><span class="date" style="color:var(--pink)">DEC 2022</span>
    <div class="art" role="img" aria-label="Golden duotone portrait photograph" style="background:linear-gradient(160deg,#d49a1c,#b8861a 60%,#e0a326)"></div>
  </div>
  <div class="cover cover-pink" style="left:460px;top:172px">
    <span class="issue" style="color:var(--cream)">ISSUE 001</span><span class="name" style="color:var(--cream)">quirk</span><span class="date" style="color:var(--cream)">DEC 2022</span>
    <div class="art" role="img" aria-label="Purple duotone photograph of flamingos among flowers" style="background:linear-gradient(180deg,#6a3a8a,#7b3c86 60%,#b04f86)"></div>
  </div>
  <div class="cover cover-cream" style="left:766px;top:172px">
    <span class="issue" style="color:var(--purple)">ISSUE 001</span><span class="name" style="color:var(--pink)">quirk</span><span class="date" style="color:var(--purple)">DEC 2022</span>
    <div class="art" role="img" aria-label="Green duotone image of a cave opening onto misty hills" style="background:radial-gradient(ellipse at 55% 45%,#9fd3a6,#4f7a37 55%,#3f5f2a)"></div>
  </div>
  <div class="book-label" style="left:151px;top:560px">Book 1</div>
  <div class="book-label" style="left:455px;top:560px">Book 2</div>
  <div class="book-label" style="left:761px;top:560px">Book 3</div>

  <div class="cover cover-green" style="left:156px;top:633px">
    <span class="issue" style="color:var(--gold)">ISSUE 001</span><span class="name" style="color:var(--gold)">quirk</span><span class="date" style="color:var(--gold)">DEC 2022</span>
    <div class="art" role="img" aria-label="Pink and violet surreal dreamscape illustration" style="background:linear-gradient(180deg,#c04f9e,#d66aa0 60%,#e59a9a)"></div>
  </div>
  <div class="cover cover-cream" style="left:460px;top:633px">
    <span class="issue" style="color:var(--purple)">ISSUE 001</span><span class="name" style="color:var(--pink)">quirk</span><span class="date" style="color:var(--purple)">DEC 2022</span>
    <div class="art" role="img" aria-label="Olive and gold duotone portrait photograph" style="background:linear-gradient(160deg,#9a9a2a,#7f9a35 60%,#a8a233)"></div>
  </div>
  <div class="cover cover-pink" style="left:766px;top:633px">
    <span class="issue" style="color:var(--cream)">ISSUE 001</span><span class="name" style="color:var(--cream)">quirk</span><span class="date" style="color:var(--cream)">DEC 2022</span>
    <div class="art" role="img" aria-label="Purple duotone photograph of a heart-shaped cloud at dusk" style="background:linear-gradient(180deg,#4a2a86,#5e2f7a 65%,#7a3a6a)"></div>
  </div>
  <div class="book-label" style="left:151px;top:1022px">Book 4</div>
  <div class="book-label" style="left:455px;top:1022px">Book 5</div>
  <div class="book-label" style="left:761px;top:1022px">Book 6</div>
</section>

<section class="band" style="top:1760px;height:583px;background:var(--green)">
  <div class="photo" role="img" aria-label="Photograph of a smiling editor in a black blazer beside office shelves" style="left:131px;top:48px;width:435px;height:475px;background:linear-gradient(90deg,#c9cccd,#eceeed 55%,#dfe2e1)"></div>
  <h2 class="abs section-title" style="left:637px;top:137px">About Us</h2>
  <p class="abs body-copy" style="left:634px;top:219px;width:430px">QUIRK is an independent literary annual journal established in 2022 by Hazel Wintergate and Mereana Clift that publishes unrepentant unfiltered accounts of life, eclectic takes on the mundane ordinary, and deep dives into modern love &amp; sexuality.</p>
  <a class="btn btn-gold" href="#" style="left:637px;top:364px">READ MORE</a>
</section>

<section class="band" style="top:2343px;height:684px;background:var(--purple)">
  <div class="photo" role="img" aria-label="Photograph of a stack of books on a wooden table" style="left:130px;top:55px;width:443px;height:335px;background:linear-gradient(160deg,#8e7a62,#5f5a4a 50%,#a99270)"></div>
  <div class="photo" role="img" aria-label="Photograph of letter tiles spelling short stories on a wooden table" style="left:624px;top:55px;width:443px;height:335px;background:linear-gradient(180deg,#3b2e25,#8a5a35 45%,#c89a6c)"></div>
  <h3 class="card-title" style="left:130px;top:423px">Submission</h3>
  <p class="card-copy" style="left:172px;top:481px">We accept flash fiction, short stories and poetry. Individual entries not to mustn’t exceed 2000 words. Submitted work must be unpublished and in English.</p>
  <a class="btn btn-gold" href="#" style="left:294px;top:580px">READ MORE</a>
  <h3 class="card-title" style="left:624px;top:423px">Annual short story competition</h3>
  <p class="card-copy" style="left:666px;top:481px">Volume Alpha is interested in all that is spiritual, coincidental, or mysterious. Stories selected for this issue reflect life’s uncanny moments, those that defy explanation,</p>
  <a class="btn btn-gold" href="#" style="left:786px;top:580px">READ MORE</a>
</section>

<section class="band" style="top:3027px;height:571px;background:var(--gold)">
  <div class="photo" role="img" aria-label="Duotone silhouette of a head formed from leaves on purple" style="left:131px;top:44px;width:435px;height:475px;background:radial-gradient(ellipse at 45% 45%,#3a2a1c,#4e3326 45%,#6b3f63 75%)"></div>
  <h2 class="abs section-title" style="left:637px;top:134px">SUPPORT US</h2>
  <p class="abs body-copy" style="left:634px;top:203px;width:400px">Since our launch in 2022, we have relied upon the generous support of our creative business community in Wellington City, New Zealand. If you read us, or love our ethos, please consider a donation.</p>
  <a class="btn btn-purple" href="#" style="left:637px;top:360px">READ MORE</a>
</section>

<footer class="band" style="top:3598px;height:168px;background:var(--pink)">
  <div class="abs wordmark" style="left:131px;top:32px">quirk</div>
  <p class="abs" style="left:130px;top:118px;font-size:12px">Copyright © 2022 All Rights Reserved</p>
  <nav class="foot-links">
    <a href="#" style="left:835px;top:45px">ABOUT US</a>
    <a href="#" style="left:994px;top:45px">PURCHASE</a>
    <a href="#" style="left:835px;top:83px">SUBMISSIONS</a>
    <a href="#" style="left:994px;top:83px">CONTACT</a>
  </nav>
</footer>

</body>
</html>
```